A2 Desk calendar/planner *landscape*

We need a promotional a2 desk calendar for our customers (examples attached). Basically a marketing item so that our business is always fresh in the customer's mind sitting at their desk. It needs to be a2 Landscape as it will be a 20-page tear-off pad. Including logos, possibly images, 2020/21 calendar years, a big section in middle for writing on like examples. Business details and possibly a list of our industries and products. I have lots of images, logos and any other information visit www.brompellink.com.au to get an idea of what we do.
Industry/Entity Type
Hydraulic
Colors
Designer to choose colors to be used in the design.
Requirements
Must have
- Buisness logo, 2020 and 2021 calander year boxes like examples attached, colour themebluje and white possiby to go with the our logo. website adress phone number info. australian holiday dates . slogan "Industry chosen hose and fittings provider"
Nice to have
- public holiday dates from ; https://www.tollimark.com.au/law-compliance/laws-regulations/public-holidays

```html
<!DOCTYPE html>
<html lang="en">
<head>
<meta charset="utf-8">
<title>Brompel Hose and Fittings – June Desk Calendar</title>
<link rel="stylesheet" href="https://fonts.googleapis.com/css2?family=Oswald:wght@400;500;600;700&family=Dosis:wght@500;600;700&display=swap">
<style>
  :root {
    --sky: #35aaea;
    --sky-deep: #1e94d6;
    --panel: #dcecf7;
    --page: #f6f6f6;
    --ink: #1c1c1c;
    --rule: #b9cfdf;
    --sunday: #e2321e;
    --navy: #1d2f9c;
    --white: #ffffff;
    --photo-dark: #141414;
  }
  * { box-sizing: border-box; margin: 0; padding: 0; }
  html, body { width: 1200px; height: 818px; overflow: hidden; }
  body { background: var(--page); font-family: "Dosis", sans-serif; color: var(--ink); }

  .calendar-page { position: relative; width: 1200px; height: 818px; background: var(--page); overflow: hidden; }
  .brand-band { position: absolute; inset: 0; width: 1200px; height: 818px; }

  /* Month block */
  .month-tab {
    position: absolute; left: 60px; top: 140px; width: 330px; height: 120px;
    background: var(--sky); border-radius: 18px 18px 0 0;
  }
  .month-name {
    position: absolute; left: 96px; top: 156px;
    font-family: "Oswald", sans-serif; font-weight: 600; font-size: 54px; line-height: 1;
    color: var(--white); letter-spacing: 1px;
  }
  .year {
    position: absolute; left: 410px; top: 70px;
    font-family: "Oswald", sans-serif; font-weight: 700; font-size: 100px;
    color: var(--sky-deep); line-height: 1;
  }
  .month-panel {
    position: absolute; left: 60px; top: 228px; width: 560px; height: 432px;
    background: var(--panel); border-radius: 22px;
  }
  .month-grid {
    position: absolute; left: 85px; top: 250px; width: 510px;
    display: grid; grid-template-columns: repeat(7, 1fr); row-gap: 16px;
    text-align: center; align-items: center;
  }
  .weekday { font-family: "Oswald", sans-serif; font-weight: 600; font-size: 30px; line-height: 1.2; }
  .day { font-family: "Dosis", sans-serif; font-weight: 500; font-size: 36px; line-height: 1.2; }
  .is-sunday { color: var(--sunday); }
  .is-holiday {
    color: var(--sunday); justify-self: center; width: 54px; height: 54px; line-height: 50px;
    border: 2px solid var(--sunday); border-radius: 50%;
  }
  .holiday-note {
    position: absolute; left: 85px; top: 622px;
    font-family: "Dosis", sans-serif; font-weight: 600; font-size: 16px; color: var(--sunday);
  }

  /* Writing area */
  .notes { position: absolute; left: 60px; top: 676px; width: 560px; }
  .notes-title {
    font-family: "Oswald", sans-serif; font-weight: 500; font-size: 18px;
    color: var(--sky-deep); text-transform: uppercase; letter-spacing: 1px;
  }
  .notes-line { height: 30px; border-bottom: 1.5px solid var(--rule); }

  /* Business side */
  .brand-plate {
    position: absolute; left: 730px; top: 40px; width: 420px; height: 100px;
    background: var(--white); border-radius: 16px;
    display: flex; align-items: center; gap: 18px; padding: 0 24px;
  }
  .brand-dot { width: 60px; height: 60px; border-radius: 50%; background: var(--navy); flex: none; }
  .brand-name {
    font-family: "Oswald", sans-serif; font-weight: 600; font-size: 31px;
    color: var(--navy); line-height: 1.05; text-transform: uppercase;
  }
  .slogan {
    position: absolute; left: 735px; top: 154px; width: 420px;
    font-family: "Oswald", sans-serif; font-weight: 500; font-size: 22px;
    color: var(--white); line-height: 1.2;
  }
  .tagline {
    position: absolute; left: 735px; top: 190px; width: 420px;
    font-family: "Dosis", sans-serif; font-weight: 500; font-size: 17px;
    color: var(--white); line-height: 1.35;
  }
  .photo {
    position: absolute; border-radius: 50%; border: 6px solid var(--white);
    background: radial-gradient(circle at 50% 45%, #3a3a3a 0%, var(--photo-dark) 70%);
  }
  .photo--hoses { left: 935px; top: 250px; width: 215px; height: 215px; }
  .photo--valve { left: 760px; top: 395px; width: 225px; height: 225px; }

  /* Next-year mini month */
  .mini-month {
    position: absolute; left: 700px; top: 640px; width: 200px; height: 160px;
    background: var(--white); border-radius: 12px; padding: 8px 9px;
  }
  .mini-title {
    font-family: "Oswald", sans-serif; font-weight: 600; font-size: 15px;
    color: var(--sky-deep); text-align: center; line-height: 1.2;
  }
  .mini-grid {
    display: grid; grid-template-columns: repeat(7, 1fr); text-align: center;
    font-family: "Dosis", sans-serif; font-weight: 600; font-size: 12px; line-height: 18px;
  }
  .mini-grid .weekday { font-size: 12px; line-height: 18px; }

  .contact {
    position: absolute; right: 50px; top: 690px; text-align: right;
    color: var(--white);
  }
  .contact-phone { font-family: "Oswald", sans-serif; font-weight: 500; font-size: 30px; line-height: 1.2; }
  .contact-email, .contact-web { font-family: "Dosis", sans-serif; font-weight: 600; font-size: 18px; line-height: 1.4; }
</style>
</head>
<body>
<main class="calendar-page">
  <svg class="brand-band" viewBox="0 0 1200 818" aria-hidden="true">
    <polygon points="700,0 1200,0 1200,818 650,818" fill="var(--sky)"/>
  </svg>

  <div class="month-tab"></div>
  <div class="month-panel"></div>
  <h1 class="month-name">JUNE</h1>
  <div class="year">2020</div>

  <div class="month-grid">
    <span class="weekday">M</span><span class="weekday">T</span><span class="weekday">W</span><span class="weekday">T</span><span class="weekday">F</span><span class="weekday">S</span><span class="weekday is-sunday">S</span>
    <span class="day">1</span><span class="day">2</span><span class="day">3</span><span class="day">4</span><span class="day">5</span><span class="day">6</span><span class="day is-sunday">7</span>
    <span class="day is-holiday">8</span><span class="day">9</span><span class="day">10</span><span class="day">11</span><span class="day">12</span><span class="day">13</span><span class="day is-sunday">14</span>
    <span class="day">15</span><span class="day">16</span><span class="day">17</span><span class="day">18</span><span class="day">19</span><span class="day">20</span><span class="day is-sunday">21</span>
    <span class="day">22</span><span class="day">23</span><span class="day">24</span><span class="day">25</span><span class="day">26</span><span class="day">27</span><span class="day is-sunday">28</span>
    <span class="day">29</span><span class="day">30</span>
  </div>
  <p class="holiday-note">Public holiday: Mon 8 June – Queen's Birthday</p>

  <section class="notes" aria-label="Notes">
    <h2 class="notes-title">Notes</h2>
    <div class="notes-line"></div>
    <div class="notes-line"></div>
    <div class="notes-line"></div>
  </section>

  <div class="brand-plate">
    <span class="brand-dot"></span>
    <span class="brand-name">Brompel<br>Hose and Fittings</span>
  </div>
  <p class="slogan">Industry chosen hose and fittings provider</p>
  <p class="tagline">Your one-stop shop in solutions for hydraulic/industrial hoses, fittings and fluid transfer products.</p>

  <div class="photo photo--hoses" role="img" aria-label="Photo of coloured industrial hoses with crimped metal fittings"></div>
  <div class="photo photo--valve" role="img" aria-label="Photo of a hydraulic directional control valve bank with levers"></div>

  <section class="mini-month" aria-label="June 2021">
    <h3 class="mini-title">JUNE 2021</h3>
    <div class="mini-grid">
      <span class="weekday">M</span><span class="weekday">T</span><span class="weekday">W</span><span class="weekday">T</span><span class="weekday">F</span><span class="weekday">S</span><span class="weekday is-sunday">S</span>
      <span></span><span>1</span><span>2</span><span>3</span><span>4</span><span>5</span><span class="is-sunday">6</span>
      <span>7</span><span>8</span><span>9</span><span>10</span><span>11</span><span>12</span><span class="is-sunday">13</span>
      <span class="is-sunday">14</span><span>15</span><span>16</span><span>17</span><span>18</span><span>19</span><span class="is-sunday">20</span>
      <span>21</span><span>22</span><span>23</span><span>24</span><span>25</span><span>26</span><span class="is-sunday">27</span>
      <span>28</span><span>29</span><span>30</span>
    </div>
  </section>

  <div class="contact">
    <div class="contact-phone">Ph: 0400 555 123</div>
    <div class="contact-email">email: hello@brompellink.com.au</div>
    <div class="contact-web">www.brompellink.com.au</div>
  </div>
</main>
</body>
</html>
```